Hydraulics Company Business Card Design

Modern business card design for a hydraulics company.
Our company colours are - black, orange and white.
I would like the following contact details included-
Name
Position
Phone number
Email
Website
Street Address

I have attached our company logo.
I would like the back of the card white.

Thank you.

```html
<!DOCTYPE html>
<html lang="en">
<head>
<meta charset="utf-8">
<title>Riverbend Hydraulics – Business Card</title>
<link href="https://fonts.googleapis.com/css2?family=Montserrat:wght@400;500;800&display=swap" rel="stylesheet">
<style>
  :root {
    --backdrop: #d2d7d7;
    --card: #f4f4f2;
    --orange: #f99d1c;
    --orange-edge: #e8860f;
    --ink: #1c1c1c;
  }
  * { margin: 0; padding: 0; box-sizing: border-box; }
  html, body { width: 1200px; height: 881px; overflow: hidden; }
  body {
    background: var(--backdrop);
    font-family: "Montserrat", sans-serif;
    position: relative;
  }
  .card {
    position: absolute;
    top: 286px;
    width: 540px;
    height: 309px;
    background: var(--card);
    border-bottom: 3px solid var(--orange-edge);
    box-shadow: 0 18px 40px rgba(60, 70, 70, 0.25);
  }
  .card--front { left: 40px; }
  .card--back { left: 620px; }

  .wordmark {
    color: var(--orange);
    font-weight: 800;
    line-height: 1.05;
    display: flex;
    align-items: center;
    gap: 12px;
  }
  .wordmark__square {
    width: 14px; height: 14px;
    background: var(--orange);
    flex: none;
  }

  .card--front .wordmark {
    position: absolute;
    left: 34px; top: 118px;
    font-size: 25px;
  }
  .divider {
    position: absolute;
    left: 268px; top: 54px;
    width: 2px; height: 200px;
    background: var(--orange);
  }
  .contact {
    position: absolute;
    left: 292px; top: 58px;
    color: var(--ink);
    font-size: 12.5px;
    line-height: 1.5;
  }
  .contact__name {
    color: var(--orange);
    font-weight: 800;
    font-size: 21px;
    line-height: 1.2;
  }
  .contact__role { margin-bottom: 12px; }
  .contact__address { margin-bottom: 12px; }
  .contact__row { display: flex; align-items: center; gap: 8px; }
  .contact__row svg { width: 11px; height: 11px; flex: none; }

  .card--back .wordmark {
    position: absolute;
    left: 0; right: 0; top: 0; bottom: 0;
    justify-content: center;
    font-size: 40px;
  }
  .card--back .wordmark__square { width: 22px; height: 22px; }
</style>
</head>
<body>

<section class="card card--front" aria-label="Card front with contact details">
  <div class="wordmark"><span class="wordmark__square"></span><span>Riverbend<br>Hydraulics</span></div>
  <div class="divider"></div>
  <div class="contact">
    <p class="contact__name">Daniel Harper</p>
    <p class="contact__role">Managing Director</p>
    <p class="contact__address">Your address, City<br>State, Zip 1234</p>
    <p class="contact__row">
      <svg viewBox="0 0 12 12" fill="var(--orange)"><path d="M2.5 1l2 2.2-1 1.3a7 7 0 0 0 4 4l1.3-1 2.2 2-1.2 1.5C5 11 1 7 1 2.3z"/></svg>
      123 456 789
    </p>
    <p class="contact__row">
      <svg viewBox="0 0 12 12"><rect x="0.5" y="2" width="11" height="8" fill="var(--orange)"/><path d="M0.8 2.3L6 6.5l5.2-4.2" stroke="#fff" stroke-width="1" fill="none"/></svg>
      info@yourgmail.com
    </p>
    <p class="contact__row">
      <svg viewBox="0 0 12 12" fill="none" stroke="var(--orange)" stroke-width="1.2"><circle cx="6" cy="6" r="5"/><ellipse cx="6" cy="6" rx="2.2" ry="5"/><path d="M1 6h10"/></svg>
      www.yourwebsite.com
    </p>
  </div>
</section>

<section class="card card--back" aria-label="Card back with company name">
  <div class="wordmark"><span class="wordmark__square"></span><span>Riverbend<br>Hydraulics</span></div>
</section>

</body>
</html>
```